I need a business logo and business card design for a new company in Alder Springs, Northvale called 'Brightwell Clinic'. Brightwell Clinic is a primary care and walk-in clinic. The logo should have the letters 'BW' connected together. The letter 'F' should be navy blue and the letter 'C' should be orange. I have attached a several business cards and the logo should be simple and memorable. I like the Harrowgate Clinic font for my card. The card should have the simplicity of Harrowgate Clinic.

The logo should be on the upper left and the name 'Brightwell Clinic' should be next to the logo.

My name Dr. Tomas Lindqvist should be in the center of the card aligned left.
Dr. Tomas Lindqvist
Board Certified in Internal Medicine
Medical Director

The bottom left should have my address.
2917 Maple Hollow Court
Suite C
Alder Springs, Northvale 22981

The bottom right should have my phone number and fax number.
Ph 555-014-2736
Fax 555-014-8490

The back of the card should have serve as an appointment reminder.
Appointment
For ____________________________________________
On _______________________at ___________________AM / PM
With ___________________________________________

If you are unable to keep your appointment, please give us 24 hour notice at 555-014-2736. Thank you.

```html
<!DOCTYPE html>
<html lang="en">
<head>
<meta charset="utf-8">
<title>Brightwell Clinic – Business Card</title>
<link href="https://fonts.googleapis.com/css2?family=Source+Sans+3:ital,wght@0,400;0,600;0,700;1,400;1,700&display=swap" rel="stylesheet">
<style>
  :root {
    --navy: #13123f;
    --orange: #e2690f;
    --ink: #3a3a3a;
    --rule: #4a4a4a;
    --paper: #f8f8f8;
    --backdrop: #e6e6e6;
  }
  * { box-sizing: border-box; margin: 0; padding: 0; }
  html, body { width: 1200px; height: 750px; overflow: hidden; }
  body {
    background: var(--backdrop);
    font-family: "Source Sans 3", sans-serif;
    position: relative;
  }
  .card {
    position: absolute;
    top: 228px;
    width: 461px;
    height: 262px;
    background: var(--paper);
    overflow: hidden;
  }
  .card--front { left: 124px; }
  .card--back { left: 618px; }

  /* Brand */
  .brand { position: absolute; display: flex; align-items: center; gap: 8px; }
  .brand__square { width: 14px; height: 14px; background: var(--orange); flex: none; }
  .brand__name {
    color: var(--navy);
    font-weight: 400;
    line-height: 0.95;
  }
  .card--front .brand { left: 27px; top: 36px; }
  .card--front .brand__name { font-size: 29px; }
  .card--back .brand { right: 34px; top: 24px; }
  .card--back .brand__name { font-size: 24px; }

  /* Front */
  .doctor { position: absolute; left: 0; right: 0; top: 140px; text-align: center; }
  .doctor__name { color: var(--navy); font-weight: 600; font-size: 17px; }
  .doctor__title { color: var(--orange); font-size: 12.5px; margin-top: 1px; }

  .address {
    position: absolute; left: 28px; top: 197px;
    font-size: 11px; line-height: 17px; color: var(--ink);
    font-style: normal;
  }
  .contact {
    position: absolute; right: 29px; top: 199px;
    font-size: 11px; line-height: 17.5px; color: var(--ink);
    list-style: none;
  }
  .contact li { display: flex; align-items: center; gap: 5px; }
  .contact svg { width: 12px; height: 12px; fill: var(--navy); }

  .band { position: absolute; left: 0; right: 0; bottom: 0; height: 18px; display: flex; }
  .band__navy { width: 342px; background: var(--navy); }
  .band__mark { width: 18px; background: #fff; display: flex; align-items: center; justify-content: center; }
  .band__mark span { width: 8px; height: 8px; background: var(--orange); }
  .band__orange { flex: 1; background: var(--orange); }

  /* Back */
  .appointment__title {
    position: absolute; left: 30px; top: 28px;
    font-size: 23px; font-weight: 700; color: var(--navy);
  }
  .field {
    position: absolute; left: 29px; right: 33px;
    display: flex; align-items: flex-end;
    font-size: 14px; color: var(--navy);
  }
  .field__line { flex: 1; border-bottom: 1px solid var(--rule); height: 1px; margin: 0 3px 4px 2px; }
  .field__suffix { font-size: 10px; }
  .field--for { top: 86px; }
  .field--when { top: 126px; }
  .field--with { top: 169px; }
  .field__gap { margin-left: 2px; }
  .notice {
    position: absolute; left: 0; right: 0; top: 206px;
    text-align: center; font-style: italic;
    font-size: 15px; line-height: 19px; color: var(--navy);
  }
  .notice strong { font-weight: 700; }
</style>
</head>
<body>

<section class="card card--front" aria-label="Business card front">
  <div class="brand">
    <span class="brand__square"></span>
    <span class="brand__name">Brightwell<br>Clinic</span>
  </div>

  <div class="doctor">
    <p class="doctor__name">Dr. Tomas Lindqvist</p>
    <p class="doctor__title">Board Certified in Internal Medicine | Medical Director</p>
  </div>

  <address class="address">
    2917 Maple Hollow Court, Suite C<br>
    Alder Springs, Northvale 22981
  </address>

  <ul class="contact">
    <li>
      <svg viewBox="0 0 24 24" aria-hidden="true"><path d="M6.6 10.8a15.1 15.1 0 0 0 6.6 6.6l2.2-2.2c.3-.3.7-.4 1-.2 1.1.4 2.3.6 3.6.6.6 0 1 .4 1 1V20c0 .6-.4 1-1 1A17 17 0 0 1 3 4c0-.6.4-1 1-1h3.5c.6 0 1 .4 1 1 0 1.3.2 2.5.6 3.6.1.3 0 .7-.2 1z"/></svg>
      <span>555-014-2736</span>
    </li>
    <li>
      <svg viewBox="0 0 24 24" aria-hidden="true"><path d="M6 2h10l2 2v5H6zM3 10h18a1 1 0 0 1 1 1v8H2v-8a1 1 0 0 1 1-1zm2 3v2h4v-2zM4 20h16v2H4z"/></svg>
      <span>555-014-8490</span>
    </li>
  </ul>

  <div class="band">
    <div class="band__navy"></div>
    <div class="band__mark"><span></span></div>
    <div class="band__orange"></div>
  </div>
</section>

<section class="card card--back" aria-label="Business card back, appointment reminder">
  <h1 class="appointment__title">Appointment</h1>
  <div class="brand">
    <span class="brand__square"></span>
    <span class="brand__name">Brightwell<br>Clinic</span>
  </div>

  <div class="field field--for"><span>For</span><span class="field__line"></span></div>
  <div class="field field--when">
    <span>On</span><span class="field__line"></span>
    <span class="field__gap">At</span><span class="field__line"></span>
    <span class="field__suffix">AM/PM</span>
  </div>
  <div class="field field--with"><span>With</span><span class="field__line"></span></div>

  <p class="notice">
    If you are unable to keep your appointment, please give<br>
    us 24 hour notice at <strong>555-014-2736</strong>. Thank you.
  </p>
</section>

</body>
</html>
```